Motivational Poster Design Project

I would like to create a poster with some of my favorite quotes to hang in my office. I did a similar project in 2012 and I've uploaded the top 2 designs so you can get a better idea of what I'm looking for. I will provide feedback on your design within 24 hours of receiving it.

The poster must contain the following quotes:

"You’re only given a little spark of madness. You mustn’t lose it.”
- Gareth Holloway

“The most contrarian thing of all is not to oppose the crowd but to think for yourself.”
- Marcus Dunne

"I constantly see people rise in life who are not the smartest, sometimes not even the most diligent, but they are learning machines. They go to bed every night a little wiser than they were when they got up and boy does that help, particularly when you have a long run ahead of you."
- Edwin Falk

“In theory, there’s no difference between theory and practice. But, in practice, there is.”
- Rolf K. T. Ter Horstwijk

"At the end of the day, a reactionary life is a normal life. One thing is consistent in every remarkable person: they decide to do something remarkable. Don’t let the world choose who you become."
- Kavin Ruparel

“It usually takes 3-4 months to try enough that you can do a proper 80/20 analysis, then two months to design systems to scale what *is* working.”
-Owen Blake

“Authority is 20 percent given, 80 percent taken.”
- Harold Vinske

“Your actions are consistent with the way the world occurs to you.”
- Colin Tabor

Project Deadline Extended
Reason: I am going to be travelling with no access to internet until January 5th, 2015. I am extending the project deadline until 12/31/14 and I'll make a final decision during the 1st week of January.

Target Market(s)

Personal Project

Industry/Entity Type

Learning

Requirements
Must have
• The poster will be 24" high x 36" long and printed on canvas, so the image you create needs to have a resolution of at least 2700 x 3900.
Nice to have
• I don't have an exact vision for how the poster should look, so I am totally open to you using your creativity to develop, arrange and present the content as you'd like.
• That said, I would like an image (photo or posterized image) of the person being quoted along with each quote. I do not have specific images that I would like you to use, so you will need to find the images on your own. The images don't need to be perfect... I am more interested in the poster relating the essence of the quotes and the people being quoted than I am in perfect photographic images of the people being quoted.

```html
<!DOCTYPE html>
<html lang="en">
<head>
<meta charset="utf-8">
<title>Quotes Poster</title>
<link href="https://fonts.googleapis.com/css2?family=Cabin:wght@400;500&family=Cabin+Condensed:wght@400;500&display=swap" rel="stylesheet">
<style>
  :root {
    --board-center: #3a3a3a;
    --board-mid: #2a2a2a;
    --board-edge: #161616;
    --chalk: rgba(225, 225, 220, 0.5);
    --ink: #f2f2ee;
    --pink: #f4a3c4;
    --blue: #8fd2f2;
    --yellow: #efe38a;
    --green: #bfe7a5;
    --peach: #f6c39c;
    --mint: #a9e3b6;
    --rose: #f2a6b8;
    --lavender: #c3b1ea;
    --portrait-light: #7c7c7c;
    --portrait-dark: #2e2e2e;
  }
  * { box-sizing: border-box; margin: 0; padding: 0; }
  html, body { width: 800px; height: 1200px; overflow: hidden; background: var(--board-edge); }
  .poster {
    position: relative;
    width: 800px;
    height: 1200px;
    overflow: hidden;
    background: radial-gradient(ellipse at 50% 45%, var(--board-center) 0%, var(--board-mid) 60%, var(--board-edge) 100%);
    font-family: "Cabin Condensed", "Cabin", sans-serif;
    color: var(--ink);
  }
  .frame { position: absolute; inset: 0; }
  .portrait {
    position: absolute;
    border-radius: 50%;
    background: radial-gradient(circle at 50% 42%, var(--portrait-light) 0%, #545454 38%, var(--portrait-dark) 62%, rgba(46,46,46,0) 72%);
  }
  .quote { position: absolute; white-space: nowrap; color: var(--ink); }
  .quote .line { display: block; }
  .quote .big { font-family: "Cabin", sans-serif; }
  .quote .author { font-family: "Cabin", sans-serif; font-weight: 500; }
  .right { text-align: right; }
  .c-pink { color: var(--pink); }
  .c-blue { color: var(--blue); }
  .c-yellow { color: var(--yellow); }
  .c-green { color: var(--green); }
  .c-peach { color: var(--peach); }
  .c-mint { color: var(--mint); }
  .c-rose { color: var(--rose); }
  .c-lavender { color: var(--lavender); }
  .doodle { position: absolute; }
  .chalk-sticks {
    position: absolute;
    left: 540px; top: 1044px; width: 205px; height: 150px;
    background: linear-gradient(100deg, rgba(90,180,230,0.4), rgba(150,220,120,0.4), rgba(240,120,150,0.4), rgba(190,150,230,0.4), rgba(240,200,90,0.4));
    border-radius: 14px;
  }
</style>
</head>
<body>
<main class="poster">

  <svg class="frame" width="800" height="1200" viewBox="0 0 800 1200" fill="none" stroke="var(--chalk)" stroke-width="3" stroke-linecap="round">
    <path d="M52 180 Q52 114 104 114 H190 Q240 114 252 70 Q264 22 312 22 H488 Q536 22 548 70 Q560 114 610 114 H696 Q748 114 748 180 V1030 Q748 1092 696 1092 H610 Q560 1092 548 1134 Q536 1180 488 1180 H312 Q264 1180 252 1134 Q240 1092 190 1092 H104 Q52 1092 52 1030 Z"/>
    <path d="M68 184 Q68 130 110 130 H196 Q252 130 264 82 Q274 38 316 38 H484 Q526 38 536 82 Q548 130 604 130 H690 Q732 130 732 184 V1026 Q732 1076 690 1076 H604 Q548 1076 536 1122 Q526 1164 484 1164 H316 Q274 1164 264 1122 Q252 1076 196 1076 H110 Q68 1076 68 1026 Z" stroke-width="2"/>
  </svg>

  <div class="portrait" role="img" aria-label="Portrait of Gareth Holloway" style="left:160px;top:178px;width:140px;height:140px;"></div>
  <p class="quote" style="left:318px;top:196px;font-size:13.5px;line-height:27px;">
    <span class="line">“You’re only given a <span class="big" style="font-size:20px;">little spark</span> of madness.</span>
    <span class="line">You mustn’t <span class="big" style="font-size:20px;">lose</span> it.” &nbsp;<span class="author c-pink" style="font-size:14px;">- Gareth Holloway</span></span>
  </p>
  <div class="doodle" role="img" aria-label="Chalk light bulb doodle" style="left:586px;top:236px;width:30px;height:38px;border-radius:50%;background:rgba(240,160,190,0.25);"></div>

  <div class="portrait" role="img" aria-label="Portrait of Marcus Dunne" style="left:558px;top:288px;width:124px;height:124px;"></div>
  <p class="quote right" style="right:258px;top:292px;font-size:13.5px;line-height:28px;">
    <span class="line">“The most <span class="big" style="font-size:20px;">contrarian</span> thing of all</span>
    <span class="line">is not to oppose the crowd but <span class="big" style="font-size:20px;">to think</span></span>
    <span class="line"><span class="big" style="font-size:20px;">for yourself</span>.” <span class="author c-blue" style="font-size:14px;">- Marcus Dunne</span></span>
  </p>
  <div class="doodle" role="img" aria-label="Chalk speech bubbles doodle" style="left:262px;top:348px;width:64px;height:38px;border-radius:10px;background:rgba(140,210,240,0.22);"></div>

  <div class="portrait" role="img" aria-label="Portrait of Edwin Falk" style="left:120px;top:414px;width:116px;height:116px;"></div>
  <p class="quote" style="left:246px;top:420px;font-size:11.5px;line-height:23px;">
    <span class="line">“I constantly see people rise in life who are not the <span class="big" style="font-size:15px;">smartest</span>, sometimes</span>
    <span class="line">not even the most <span class="big" style="font-size:15px;">diligent</span>, but they are <span class="big" style="font-size:15px;">learning machines</span>. They go to bed</span>
    <span class="line">every night a little <span class="big" style="font-size:15px;">wiser</span> than they were when they got up and boy does that help,</span>
    <span class="line">particularly when you have <span class="big" style="font-size:15px;">a long run ahead of you</span>.”</span>
    <span class="line"><span class="author c-yellow" style="font-size:13.5px;">- Edwin Falk</span></span>
  </p>
  <svg class="doodle" style="left:636px;top:452px;" width="40" height="32" viewBox="0 0 44 34" fill="none" stroke="var(--yellow)" stroke-width="2" stroke-linecap="round" stroke-linejoin="round">
    <path d="M2 32 L14 20 L22 24 L40 4"/><path d="M30 4 H40 V14"/>
  </svg>

  <div class="portrait" role="img" aria-label="Portrait of Rolf K. T. Ter Horstwijk" style="left:548px;top:518px;width:120px;height:120px;"></div>
  <p class="quote" style="left:222px;top:540px;font-size:13px;line-height:38px;">
    <span class="line">“<span class="big" style="font-size:20px;">In theory</span>, there’s no between theory and practice. But,</span>
    <span class="line"><span class="big" style="font-size:20px;">in practice</span>, there is.” &nbsp;<span class="author c-green" style="font-size:13.5px;">- Rolf K. T. Ter Horstwijk</span></span>
  </p>
  <div class="doodle" role="img" aria-label="Chalk pencil doodle" style="left:514px;top:540px;width:28px;height:22px;border-radius:6px;background:rgba(190,230,170,0.22);"></div>

  <div class="portrait" role="img" aria-label="Portrait of Kavin Ruparel" style="left:126px;top:622px;width:124px;height:124px;"></div>
  <p class="quote" style="left:266px;top:650px;font-size:11px;line-height:27px;">
    <span class="line">“At the end of the day, a reactionary life is a <span class="big" style="font-size:15px;">normal life</span>.</span>
    <span class="line">One thing is consistent in every <span class="big" style="font-size:15px;">remarkable person</span>:</span>
    <span class="line">they decide to do something remarkable. <span class="big" style="font-size:15px;">Don’t let the</span></span>
    <span class="line"><span class="big" style="font-size:15px;">world choose who you become</span>.” <span class="author c-peach" style="font-size:13px;">- Kavin Ruparel</span></span>
  </p>
  <div class="doodle" role="img" aria-label="Chalk globe doodle" style="left:560px;top:658px;width:38px;height:46px;border-radius:50%;background:rgba(246,195,156,0.22);"></div>

  <div class="portrait" role="img" aria-label="Portrait of Owen Blake" style="left:616px;top:720px;width:124px;height:124px;"></div>
  <p class="quote right" style="right:212px;top:776px;font-size:12px;line-height:27px;">
    <span class="line">“It usually takes <span class="big" style="font-size:16px;">3-4 months</span> to try enough</span>
    <span class="line">that you can do a proper 80/20 analysis, then</span>
    <span class="line"><span class="big" style="font-size:16px;">two months</span> to design systems to scale</span>
    <span class="line"><span class="big" style="font-size:16px;">what *is* working</span>.” <span class="author c-mint" style="font-size:13.5px;">- Owen Blake</span></span>
  </p>
  <svg class="doodle" style="left:294px;top:800px;" width="66" height="48" viewBox="0 0 74 52" fill="none" stroke="var(--yellow)" stroke-width="1.8" stroke-linecap="round" stroke-linejoin="round">
    <path d="M4 2 V48 H72"/><path d="M8 42 L22 28 L32 34 L46 16 L56 24 L68 8"/><path d="M8 46 L22 38 L34 40 L48 30 L66 26" stroke="var(--mint)"/>
  </svg>

  <div class="portrait" role="img" aria-label="Portrait of Harold Vinske" style="left:96px;top:826px;width:120px;height:120px;"></div>
  <p class="quote" style="left:222px;top:908px;font-size:13px;line-height:28px;">
    <span class="line">“Authority is <span class="big" style="font-size:19px;">20</span> percent <span class="big" style="font-size:19px;">given</span>,</span>
    <span class="line"><span class="big" style="font-size:19px;">80</span> percent <span class="big" style="font-size:19px;">taken</span>.” &nbsp;<span class="author c-rose" style="font-size:13.5px;">- Harold Vinske</span></span>
  </p>
  <div class="doodle" role="img" aria-label="Chalk pen doodle" style="left:476px;top:914px;width:14px;height:44px;border-radius:6px;background:rgba(242,166,184,0.25);"></div>

  <div class="portrait" role="img" aria-label="Portrait of Colin Tabor" style="left:518px;top:884px;width:120px;height:120px;"></div>
  <svg class="doodle" style="left:246px;top:1002px;" width="50" height="50" viewBox="0 0 50 50" fill="none" stroke="var(--lavender)" stroke-width="1.6">
    <circle cx="25" cy="25" r="14"/><path d="M25 2 L29 21 L48 25 L29 29 L25 48 L21 29 L2 25 L21 21 Z"/>
  </svg>
  <p class="quote" style="left:342px;top:1000px;font-size:12.5px;line-height:22px;">
    <span class="line">“Your <span class="big" style="font-size:17px;">actions</span> are <span class="big" style="font-size:17px;">consistent</span></span>
    <span class="line">with the way the world occurs to you.”</span>
    <span class="line" style="padding-left:44px;"><span class="author c-lavender" style="font-size:13.5px;">- Colin Tabor</span></span>
  </p>

  <div class="chalk-sticks" role="img" aria-label="Five coloured chalk sticks lying in a row"></div>

</main>
</body>
</html>
```